Business Card Design

Company is a Commercial Building Company specialising in New Construction and existing refurbishments

Business

Contact Information for Business Card

Derek Halloway
Construction Manager
E Derek@ridgemarkbuilding.com.au
M 0400 215 397
Mail 14 Tarrington Loop Brackenvale NV 6938

```html
<!DOCTYPE html>
<html lang="en">
<head>
<meta charset="utf-8">
<title>Ridgemark Building &amp; Construction – Business Card</title>
<link rel="stylesheet" href="https://fonts.googleapis.com/css2?family=Open+Sans:ital,wght@0,400;1,400&family=Saira:wght@500;600&display=swap">
<style>
  :root {
    --backdrop: #e9e6e1;
    --card: #f7f7f7;
    --slate: #3d4a5c;
    --blue: #1aa6c8;
    --ink: #333d4a;
    --white: #ffffff;
  }
  * { margin: 0; padding: 0; box-sizing: border-box; }
  html, body { width: 1200px; height: 804px; overflow: hidden; }
  body { background: var(--backdrop); position: relative; font-family: "Open Sans", Arial, sans-serif; }

  .card {
    position: absolute;
    top: 257px;
    width: 478px;
    height: 288px;
    background: var(--card);
    box-shadow: 0 2px 6px rgba(0,0,0,0.18);
    overflow: hidden;
  }
  .card--front { left: 108px; }
  .card--back { left: 613px; }

  /* Front */
  .front-square {
    position: absolute;
    left: 209px; top: 84px;
    width: 60px; height: 60px;
    background: var(--blue);
  }
  .front-name {
    position: absolute;
    left: 0; right: 0; top: 178px;
    text-align: center;
    font-family: "Saira", Arial, sans-serif;
    font-weight: 500;
    color: var(--slate);
    line-height: 1.08;
  }
  .front-name__main { display: block; font-size: 25px; letter-spacing: 0.3px; }
  .front-name__sub { display: block; font-size: 21px; }

  /* Back */
  .brand {
    position: absolute;
    left: 25px; top: 30px;
    display: flex; align-items: center;
  }
  .brand__square { width: 50px; height: 50px; background: var(--blue); flex: none; }
  .brand__name {
    margin-left: 52px;
    font-family: "Saira", Arial, sans-serif;
    font-weight: 500;
    color: var(--slate);
    line-height: 1.08;
  }
  .brand__main { display: block; font-size: 23px; letter-spacing: 0.2px; }
  .brand__sub { display: block; font-size: 20px; }

  .person { position: absolute; left: 25px; top: 138px; }
  .person__name {
    font-family: "Saira", Arial, sans-serif;
    font-weight: 600;
    font-size: 21px;
    letter-spacing: 1.5px;
    color: var(--slate);
    text-transform: uppercase;
    line-height: 1.1;
  }
  .person__role { font-style: italic; font-size: 14px; color: var(--blue); margin-top: 1px; }

  .contact { position: absolute; left: 25px; top: 192px; list-style: none; }
  .contact__item {
    display: flex; align-items: center; gap: 11px;
    font-size: 13px; color: var(--ink); height: 18px;
  }
  .contact__icon { width: 13px; height: 13px; flex: none; }

  .address-band {
    position: absolute;
    left: 0; right: 0; bottom: 0;
    height: 38px;
    background: var(--slate);
    color: var(--white);
    font-size: 13px;
    padding: 6px 25px 0;
  }
</style>
</head>
<body>
  <section class="card card--front">
    <span class="front-square"></span>
    <p class="front-name">
      <span class="front-name__main">RIDGEMARK BUILDING</span>
      <span class="front-name__sub">&amp; CONSTRUCTION</span>
    </p>
  </section>

  <section class="card card--back">
    <div class="brand">
      <span class="brand__square"></span>
      <p class="brand__name">
        <span class="brand__main">RIDGEMARK BUILDING</span>
        <span class="brand__sub">&amp; CONSTRUCTION</span>
      </p>
    </div>

    <div class="person">
      <h1 class="person__name">Derek Halloway</h1>
      <p class="person__role">Construction Manager</p>
    </div>

    <ul class="contact">
      <li class="contact__item">
        <svg class="contact__icon" viewBox="0 0 13 13" aria-hidden="true"><rect x="3" y="0.5" width="7" height="12" rx="1.2" fill="none" stroke="#1aa6c8" stroke-width="1.3"/><circle cx="6.5" cy="10.3" r="0.8" fill="#1aa6c8"/></svg>
        0400 215 397
      </li>
      <li class="contact__item">
        <svg class="contact__icon" viewBox="0 0 13 13" aria-hidden="true"><rect x="0.5" y="2.5" width="12" height="8" fill="#1aa6c8"/><path d="M0.5 2.5 L6.5 7 L12.5 2.5" fill="none" stroke="#f7f7f7" stroke-width="1"/></svg>
        Derek@ridgemarkbuilding.com.au
      </li>
      <li class="contact__item">
        <svg class="contact__icon" viewBox="0 0 13 13" aria-hidden="true"><circle cx="6.5" cy="6.5" r="5.5" fill="none" stroke="#1aa6c8" stroke-width="1.2"/><ellipse cx="6.5" cy="6.5" rx="2.4" ry="5.5" fill="none" stroke="#1aa6c8" stroke-width="1"/><line x1="1" y1="6.5" x2="12" y2="6.5" stroke="#1aa6c8" stroke-width="1"/></svg>
        www.ridgemarkbuilding.com.au
      </li>
    </ul>

    <p class="address-band">14 Tarrington Loop Brackenvale NV 6938</p>
  </section>
</body>
</html>
```